Design a poster that illustrates the six central pillars of our school district's efforts with students. The attached PDF outlines the six main competencies we aim for students to possess upon graduation. Each of the 6 has 3 bullet points for the poster as well. The title is "Profile of a Kestrel". Our mascot is this attached winged wheel. The overall concept is that staff take kids when they are young and develop these 6 things when they graduate. Our colors are navy, red, and white. We will make this poster in a variety of sizes in offices, classrooms, and in digital spaces as well. On the PDF - ignore the column that says "Synthesis". That has nothing to do with this poster.

The district is Harlow Creek Public Schools https://www.harlowcreek-schools.example/

```html
<!DOCTYPE html>
<html lang="en">
<head>
<meta charset="utf-8">
<title>Profile of a Kestrel — Harlow Creek Public Schools</title>
<link rel="stylesheet" href="https://fonts.googleapis.com/css2?family=Inter:wght@400;500&family=Montserrat:wght@800&family=Nunito:wght@900&family=Outfit:wght@300;400&family=Dancing+Script:wght@700&display=swap">
<style>
  :root {
    --navy: #23304a;
    --navy-deep: #1c2840;
    --red: #8f1d24;
    --red-light: #a82a33;
    --white: #ffffff;
    --ink: #2a2d35;
    --pale: #ececee;
    --stage: #8b8b8b;
    --sun-top: #f39a45;
    --sun-mid: #e66a22;
    --dusk: #4a2212;
    --ground: #0e0c0b;
    --accent-orange: #f28a2a;
  }
  * { margin: 0; padding: 0; box-sizing: border-box; }
  html, body { width: 984px; height: 1200px; overflow: hidden; }
  body { background: var(--stage); font-family: "Outfit", sans-serif; color: var(--ink); }

  .poster {
    position: absolute; left: 72px; top: 80px;
    width: 817px; height: 1058px;
    background: var(--white); overflow: hidden;
  }
  .hero-photo {
    position: absolute; left: 0; top: 0; width: 817px; height: 600px;
    background: linear-gradient(180deg, var(--sun-top) 0%, var(--sun-mid) 38%, #c9521c 50%, var(--dusk) 57%, var(--ground) 66%, var(--ground) 100%);
  }
  .poster-shapes { position: absolute; left: 0; top: 0; width: 817px; height: 1058px; }

  .district {
    position: absolute; left: 115px; top: 40px;
  }
  .district-name { font-family: "Inter", sans-serif; font-weight: 500; font-size: 18px; color: var(--navy); letter-spacing: .2px; }
  .district-tagline { font-family: "Inter", sans-serif; font-weight: 400; font-size: 11.6px; color: var(--ink); margin-top: 3px; }

  .title-bubble { position: absolute; left: 27px; top: 227px; width: 358px; height: 182px; }
  .title {
    position: absolute; left: 70px; top: 250px; width: 280px;
    font-family: "Montserrat", sans-serif; font-weight: 800; color: var(--white);
    font-size: 55px; line-height: 66px; letter-spacing: 0;
  }
  .title span { display: block; }
  .title .title-link {
    position: absolute; left: 105px; top: 45px;
    font-family: "Dancing Script", cursive; font-weight: 700;
    color: var(--red-light); font-size: 44px; line-height: 1;
  }

  .trait-head { position: absolute; height: 76px; }
  .trait-bar {
    position: absolute; top: 23px; left: 38px; height: 30px;
    background: linear-gradient(90deg, var(--red) 0%, var(--red-light) 60%, var(--red) 100%);
    border-radius: 0 16px 16px 0;
  }
  .trait-name {
    position: absolute; left: 45px; top: 20px;
    font-family: "Nunito", sans-serif; font-weight: 900; font-size: 25px; line-height: 34px;
    color: var(--white); white-space: nowrap;
  }
  .trait-icon {
    position: absolute; left: 0; top: 0; width: 76px; height: 76px; border-radius: 50%;
    background: var(--navy); border: 3px solid var(--white);
    box-shadow: 0 0 0 2px var(--red);
  }

  .point {
    position: absolute; width: 114px; padding-left: 14px;
    font-size: 11.4px; line-height: 14.4px; font-weight: 300; color: var(--ink);
  }
  .point svg { position: absolute; left: 0; top: 2px; width: 10px; height: 10px; }
  .point::after {
    content: ""; position: absolute; left: 4.5px; top: 15px; bottom: 0;
    border-left: 1px dotted var(--red);
  }

  .footer {
    position: absolute; left: 30px; top: 1009px; width: 760px; height: 49px;
    background: var(--red); border-radius: 30px 30px 0 0;
    display: flex; align-items: center; justify-content: center;
    color: var(--white); font-family: "Outfit", sans-serif; font-size: 15.6px; font-weight: 400;
  }
  .footer-item { display: flex; align-items: center; gap: 5px; padding: 0 13px; height: 100%; }
  .footer-item + .footer-item { border-left: 1px solid rgba(255,255,255,.75); }
  .footer-item svg { width: 13px; height: 13px; }
</style>
</head>
<body>
<main class="poster">
  <div class="hero-photo" role="img" aria-label="Sunset photograph: silhouette of a graduate in cap and gown walking hand in hand with a young child across a hill"></div>

  <svg class="poster-shapes" viewBox="0 0 1362 1763" aria-hidden="true">
    <defs>
      <linearGradient id="pale-wash" x1="0" y1="0" x2="0" y2="1">
        <stop offset="0" stop-color="#e9e9eb"/>
        <stop offset=".35" stop-color="#f7f7f8"/>
        <stop offset=".6" stop-color="#ffffff"/>
      </linearGradient>
    </defs>
    <path d="M0 0 H800 C640 170 330 218 0 222 Z" fill="#ffffff"/>
    <path d="M772 0 C660 140 470 205 300 214" fill="none" stroke="var(--accent-orange)" stroke-width="5"/>
    <path d="M0 600 C40 588 90 580 140 575 L140 612 C90 625 40 645 0 672 Z" fill="var(--red)"/>
    <path d="M610 520 C900 515 1220 700 1362 860 V965 C1220 780 960 600 610 548 Z" fill="var(--navy)"/>
    <path d="M0 655 C250 565 520 525 700 545 C960 575 1220 760 1362 965 V1763 H0 Z" fill="url(#pale-wash)"/>
  </svg>

  <header class="district">
    <div class="district-name">Harlow Creek Public Schools</div>
    <div class="district-tagline">Excellence in Academics, Arts &amp; Athletics</div>
  </header>

  <svg class="title-bubble" viewBox="0 0 358 182" aria-hidden="true">
    <path d="M42 0 H316 A42 42 0 0 1 358 42 V140 A42 42 0 0 1 316 182 H98 L59 212 V182 H42 A42 42 0 0 1 0 140 V42 A42 42 0 0 1 42 0 Z" fill="var(--navy)"/>
  </svg>
  <h1 class="title">
    <span>PROFILE</span>
    <span class="title-link">of a</span>
    <span>KESTREL</span>
  </h1>

  <!-- Communicator -->
  <div class="trait-head" style="left:43px;top:461px;width:302px">
    <div class="trait-bar" style="width:264px"></div>
    <div class="trait-icon" role="img" aria-label="Conversation icon"></div>
    <div class="trait-name" style="left:84px">Communicator</div>
  </div>
  <p class="point" style="left:48px;top:547px"><svg viewBox="0 0 10 10"><circle cx="5" cy="5" r="4.3" fill="none" stroke="#8f1d24" stroke-width=".9"/><path d="M3 5.1 L4.5 6.5 L7 3.8" fill="none" stroke="#8f1d24" stroke-width=".9"/></svg>Expresses ideas clearly and respectfully (written &amp; verbal).</p>
  <p class="point" style="left:167px;top:547px"><svg viewBox="0 0 10 10"><circle cx="5" cy="5" r="4.3" fill="none" stroke="#8f1d24" stroke-width=".9"/><path d="M3 5.1 L4.5 6.5 L7 3.8" fill="none" stroke="#8f1d24" stroke-width=".9"/></svg>Listens actively and understands diverse perspectives.</p>
  <p class="point" style="left:282px;top:547px;width:120px"><svg viewBox="0 0 10 10"><circle cx="5" cy="5" r="4.3" fill="none" stroke="#8f1d24" stroke-width=".9"/><path d="M3 5.1 L4.5 6.5 L7 3.8" fill="none" stroke="#8f1d24" stroke-width=".9"/></svg>Adjusts communication to suit the audience and context.</p>

  <!-- Adaptable -->
  <div class="trait-head" style="left:421px;top:464px;width:302px">
    <div class="trait-bar" style="width:264px"></div>
    <div class="trait-icon" role="img" aria-label="Gear with changing shapes icon"></div>
    <div class="trait-name" style="left:84px">Adaptable</div>
  </div>
  <p class="point" style="left:426px;top:550px"><svg viewBox="0 0 10 10"><circle cx="5" cy="5" r="4.3" fill="none" stroke="#8f1d24" stroke-width=".9"/><path d="M3 5.1 L4.5 6.5 L7 3.8" fill="none" stroke="#8f1d24" stroke-width=".9"/></svg>Responds productively to new situations, challenges, and feedback.</p>
  <p class="point" style="left:545px;top:550px"><svg viewBox="0 0 10 10"><circle cx="5" cy="5" r="4.3" fill="none" stroke="#8f1d24" stroke-width=".9"/><path d="M3 5.1 L4.5 6.5 L7 3.8" fill="none" stroke="#8f1d24" stroke-width=".9"/></svg>Learns from new experiences and applies prior knowledge in evolving contexts.</p>
  <p class="point" style="left:660px;top:550px;width:120px"><svg viewBox="0 0 10 10"><circle cx="5" cy="5" r="4.3" fill="none" stroke="#8f1d24" stroke-width=".9"/><path d="M3 5.1 L4.5 6.5 L7 3.8" fill="none" stroke="#8f1d24" stroke-width=".9"/></svg>Adjusts behavior and approach to effectively engage with diverse groups and environments.</p>

  <!-- Critical Thinker -->
  <div class="trait-head" style="left:43px;top:641px;width:302px">
    <div class="trait-bar" style="width:264px"></div>
    <div class="trait-icon" role="img" aria-label="Thinking head with key and gear icon"></div>
    <div class="trait-name" style="left:84px">Critical Thinker</div>
  </div>
  <p class="point" style="left:48px;top:726px"><svg viewBox="0 0 10 10"><circle cx="5" cy="5" r="4.3" fill="none" stroke="#8f1d24" stroke-width=".9"/><path d="M3 5.1 L4.5 6.5 L7 3.8" fill="none" stroke="#8f1d24" stroke-width=".9"/></svg>Questions, analyzes, and evaluates information from multiple sources.</p>
  <p class="point" style="left:167px;top:726px"><svg viewBox="0 0 10 10"><circle cx="5" cy="5" r="4.3" fill="none" stroke="#8f1d24" stroke-width=".9"/><path d="M3 5.1 L4.5 6.5 L7 3.8" fill="none" stroke="#8f1d24" stroke-width=".9"/></svg>Identifies and solves complex problems creatively.</p>
  <p class="point" style="left:282px;top:726px;width:124px"><svg viewBox="0 0 10 10"><circle cx="5" cy="5" r="4.3" fill="none" stroke="#8f1d24" stroke-width=".9"/><path d="M3 5.1 L4.5 6.5 L7 3.8" fill="none" stroke="#8f1d24" stroke-width=".9"/></svg>Uses evidence and diverse perspectives to form reasoned conclusions and make informed decisions.</p>

  <!-- Collaborator -->
  <div class="trait-head" style="left:421px;top:641px;width:302px">
    <div class="trait-bar" style="width:264px"></div>
    <div class="trait-icon" role="img" aria-label="Joined hands icon"></div>
    <div class="trait-name" style="left:84px">Collaborator</div>
  </div>
  <p class="point" style="left:426px;top:727px"><svg viewBox="0 0 10 10"><circle cx="5" cy="5" r="4.3" fill="none" stroke="#8f1d24" stroke-width=".9"/><path d="M3 5.1 L4.5 6.5 L7 3.8" fill="none" stroke="#8f1d24" stroke-width=".9"/></svg>Contributes effectively and cooperatively to shared goals.</p>
  <p class="point" style="left:545px;top:727px"><svg viewBox="0 0 10 10"><circle cx="5" cy="5" r="4.3" fill="none" stroke="#8f1d24" stroke-width=".9"/><path d="M3 5.1 L4.5 6.5 L7 3.8" fill="none" stroke="#8f1d24" stroke-width=".9"/></svg>Listens actively and values diverse ideas and perspectives.</p>
  <p class="point" style="left:660px;top:727px;width:126px"><svg viewBox="0 0 10 10"><circle cx="5" cy="5" r="4.3" fill="none" stroke="#8f1d24" stroke-width=".9"/><path d="M3 5.1 L4.5 6.5 L7 3.8" fill="none" stroke="#8f1d24" stroke-width=".9"/></svg>Engages respectfully, compromising and leading when appropriate.</p>

  <!-- Responsible -->
  <div class="trait-head" style="left:43px;top:821px;width:302px">
    <div class="trait-bar" style="width:264px"></div>
    <div class="trait-icon" role="img" aria-label="Hand holding a gear icon"></div>
    <div class="trait-name" style="left:84px">Responsible</div>
  </div>
  <p class="point" style="left:48px;top:906px;width:118px"><svg viewBox="0 0 10 10"><circle cx="5" cy="5" r="4.3" fill="none" stroke="#8f1d24" stroke-width=".9"/><path d="M3 5.1 L4.5 6.5 L7 3.8" fill="none" stroke="#8f1d24" stroke-width=".9"/></svg>Takes ownership of actions, choices, and commitments.</p>
  <p class="point" style="left:167px;top:906px"><svg viewBox="0 0 10 10"><circle cx="5" cy="5" r="4.3" fill="none" stroke="#8f1d24" stroke-width=".9"/><path d="M3 5.1 L4.5 6.5 L7 3.8" fill="none" stroke="#8f1d24" stroke-width=".9"/></svg>Manages time, resources, and self to meet expectations.</p>
  <p class="point" style="left:282px;top:906px;width:120px"><svg viewBox="0 0 10 10"><circle cx="5" cy="5" r="4.3" fill="none" stroke="#8f1d24" stroke-width=".9"/><path d="M3 5.1 L4.5 6.5 L7 3.8" fill="none" stroke="#8f1d24" stroke-width=".9"/></svg>Acts with integrity and advocates for self and others.</p>

  <!-- Compassionate -->
  <div class="trait-head" style="left:421px;top:821px;width:302px">
    <div class="trait-bar" style="width:264px"></div>
    <div class="trait-icon" role="img" aria-label="Hands around a heart icon"></div>
    <div class="trait-name" style="left:84px">Compassionate</div>
  </div>
  <p class="point" style="left:426px;top:906px"><svg viewBox="0 0 10 10"><circle cx="5" cy="5" r="4.3" fill="none" stroke="#8f1d24" stroke-width=".9"/><path d="M3 5.1 L4.5 6.5 L7 3.8" fill="none" stroke="#8f1d24" stroke-width=".9"/></svg>Understands and acknowledges others' feelings, perspectives, and experiences.</p>
  <p class="point" style="left:545px;top:906px"><svg viewBox="0 0 10 10"><circle cx="5" cy="5" r="4.3" fill="none" stroke="#8f1d24" stroke-width=".9"/><path d="M3 5.1 L4.5 6.5 L7 3.8" fill="none" stroke="#8f1d24" stroke-width=".9"/></svg>Responds with kindness, patience, and support.</p>
  <p class="point" style="left:660px;top:906px;width:120px"><svg viewBox="0 0 10 10"><circle cx="5" cy="5" r="4.3" fill="none" stroke="#8f1d24" stroke-width=".9"/><path d="M3 5.1 L4.5 6.5 L7 3.8" fill="none" stroke="#8f1d24" stroke-width=".9"/></svg>Seeks to connect with and contribute positively to the well-being of others and the community.</p>

  <footer class="footer">
    <div class="footer-item">
      <svg viewBox="0 0 12 12"><path d="M6 11.5 C3 8 2 6.3 2 4.5 A4 4 0 0 1 10 4.5 C10 6.3 9 8 6 11.5 Z" fill="none" stroke="#fff" stroke-width="1.2"/><circle cx="6" cy="4.5" r="1.4" fill="none" stroke="#fff" stroke-width="1.1"/></svg>
      <span>Harlow Creek Public Schools 140 North Mill St.</span>
    </div>
    <div class="footer-item">
      <svg viewBox="0 0 12 12"><circle cx="6" cy="6" r="5" fill="none" stroke="#fff" stroke-width="1"/><ellipse cx="6" cy="6" rx="2.2" ry="5" fill="none" stroke="#fff" stroke-width="1"/><path d="M1 6 H11 M2 3.5 H10 M2 8.5 H10" stroke="#fff" stroke-width=".9"/></svg>
      <span>www.harlowcreek-schools.example</span>
    </div>
    <div class="footer-item">
      <svg viewBox="0 0 12 12"><path d="M2.5 1 L4.6 1.2 L5.3 3.8 L4 4.9 C4.7 6.5 5.6 7.4 7.1 8.1 L8.2 6.8 L10.9 7.5 L11 9.6 C10.6 10.6 9.7 11 8.7 11 C4.6 10.4 1.6 7.4 1 3.3 C1 2.3 1.5 1.4 2.5 1 Z" fill="#fff"/></svg>
      <span>555-014-2270</span>
    </div>
  </footer>
</main>
</body>
</html>
```